Business Card Design Project

I require a business card with the following information on them for various different people;
name
m:
f:
e:
I have a logo already and will attached that. We are in the construction industry. I require something clean and simple but eye catching at the same time. You can use another colour with our logo if you like and you can style the logo as well if you wish. I am open.
Also it needs to be front and back design.
Industry/Entity Type
Construction
Requirements
Must have
- Logo, name, mobile, fax and email address.
Front and back design

```html
<!DOCTYPE html>
<html lang="en">
<head>
<meta charset="utf-8">
<title>Veltmoor Quarrick Works – Business Card</title>
<link rel="stylesheet" href="https://fonts.googleapis.com/css2?family=Arimo:wght@400&display=swap">
<style>
  :root {
    --bg: #ece9e4;
    --card: #ffffff;
    --green: #4cae3f;
    --ink: #3d3d3d;
    --shadow: rgba(0, 0, 0, 0.22);
  }
  * { margin: 0; padding: 0; box-sizing: border-box; }
  html, body { width: 1200px; height: 1000px; overflow: hidden; }
  body {
    background: var(--bg);
    font-family: "Arimo", Arial, sans-serif;
    position: relative;
  }
  .card-holder {
    position: absolute;
    top: 200px;
    width: 340px;
    height: 580px;
    filter: drop-shadow(0 4px 6px var(--shadow));
  }
  .card-holder--front { left: 200px; }
  .card-holder--back { left: 660px; }
  .card {
    width: 100%;
    height: 100%;
    background: var(--card);
    position: relative;
  }
  .card--front {
    clip-path: polygon(0 50px, 20px 30px, 120px 30px, 120px 15px, 135px 0, 340px 0, 340px 580px, 0 580px);
  }
  .card--back {
    clip-path: polygon(0 0, 205px 0, 220px 15px, 220px 30px, 320px 30px, 340px 50px, 340px 580px, 0 580px);
  }
  .brand {
    color: var(--green);
    font-size: 22px;
    line-height: 1.2;
    white-space: nowrap;
  }
  .brand-front {
    position: absolute;
    left: 40px;
    top: 64px;
    display: flex;
    align-items: center;
    gap: 10px;
  }
  .brand-front .brand-square {
    width: 16px;
    height: 16px;
    background: var(--green);
    flex: none;
  }
  .brand-back {
    position: absolute;
    left: 40px;
    top: 290px;
  }
  .person { position: absolute; left: 40px; top: 350px; }
  .person__name { color: var(--green); font-size: 20px; line-height: 1.2; }
  .person__role { color: var(--ink); font-size: 14px; line-height: 1.2; margin-top: 3px; }
  .contacts {
    position: absolute;
    left: 40px;
    top: 440px;
    list-style: none;
    font-size: 14px;
    color: var(--ink);
  }
  .contacts li { display: flex; gap: 12px; line-height: 20px; }
  .contacts .label { color: var(--green); width: 10px; }
</style>
</head>
<body>
  <div class="card-holder card-holder--front">
    <section class="card card--front" aria-label="Card front">
      <div class="brand brand-front"><span class="brand-square"></span><span>Veltmoor Quarrick Works</span></div>
    </section>
  </div>

  <div class="card-holder card-holder--back">
    <section class="card card--back" aria-label="Card back">
      <div class="brand brand-back">Veltmoor Quarrick Works</div>
      <div class="person">
        <p class="person__name">Employee Name</p>
        <p class="person__role">Employee Position</p>
      </div>
      <ul class="contacts">
        <li><span class="label">m</span><span>(0)10 555 210</span></li>
        <li><span class="label">f</span><span>(0)10 555 211</span></li>
        <li><span class="label">e</span><span>employee1@vqworks.com</span></li>
      </ul>
    </section>
  </div>
</body>
</html>
```